Corporate Financing/Banking Website Design

I need a website for a corporate financing website.

The company helps other companies raise money for financing.

Content for the website can be found here: https://www.plumsite.ca/northwavecapital/

Each section from the content in the main page above should have a corresponding image associated with each "Section"

1. Financing solutions that will be provided by Corven Ridge Finance will include:

2. The financing solutions mentioned above will assist businesses to:

3. The industry sectors focussed on are, but not limited to:

We need to make sure that the website has clear buttons for the visitor to "Apply Now" and "Book an Appointment" to apply for financing options.

We need the following pages designed
Home
About Us
Financing Solutions
Contact Us.

For the Logo:

The company name is Corven Ridge Finance. Something that emphasizes direction and progress and is related to Corporate finance

Something professional that conveys confidence

Target Market(s)

Corporation and large business

Logo Text

Corven Ridge Finance

Number of Pages Required

4 page

Colors
0393ce

Requirements
Must have
• Use the color: #OA64BC

Please ensure 'Apply Now' & 'Book an Appointment' buttons are very clear and placed appropriately on the webpage.

In the Footer I would like 'T&C's' and 'Privacy Policy' links

Social Media icon links will be 'Peerlane / Circlehall/ Shortwire and we should keep these in Footer and Contacts page section.
Should not have
• - Do not include a search field

```html
<!DOCTYPE html>
<html lang="en">
<head>
<meta charset="utf-8">
<title>Corven Ridge Finance</title>
<link href="https://fonts.googleapis.com/css2?family=Cinzel:wght@400;500;600&family=Roboto:wght@400;500;700&display=swap" rel="stylesheet">
<style>
:root{
  --blue:#0a64bc;
  --blue-btn:#1677c5;
  --blue-bright:#0393ce;
  --navy:#0c1a3a;
  --footer:#212c6d;
  --ink:#111111;
  --text:#666a70;
  --white:#ffffff;
}
*{margin:0;padding:0;box-sizing:border-box}
html,body{width:1200px;height:3421px;overflow:hidden;background:var(--white)}
body{position:relative;font-family:"Roboto",Arial,sans-serif;color:var(--ink)}
a{text-decoration:none}

/* header */
.topline{position:absolute;left:0;top:0;width:1200px;height:3px;background:var(--blue)}
.header{position:absolute;left:0;top:0;width:1200px;height:82px;border-bottom:1px solid #e5e5e5;background:var(--white)}
.brand{position:absolute;left:143px;top:27px;display:flex;align-items:center;gap:12px;text-decoration:none}
.brand-mark{width:24px;height:24px;background:var(--blue)}
.brand-name{font-family:"Cinzel",serif;font-weight:500;font-size:25px;color:var(--blue);letter-spacing:.3px}
.nav{position:absolute;top:0;left:568px;display:flex;height:82px}
.nav a{display:block;height:82px;line-height:84px;font-size:14px;font-weight:500;color:#1a1a1a;text-transform:uppercase}
.nav .home{background:var(--blue-btn);color:#fff;width:74px;text-align:center}
.nav .about{margin-left:23px}
.nav .solutions{margin-left:40px}
.nav .contact{margin-left:40px}

/* hero */
.hero{position:absolute;left:0;top:82px;width:1200px;height:645px;
  background:radial-gradient(ellipse 520px 300px at 720px 270px,#1d6f8a 0%,#0e3e5a 45%,transparent 75%),linear-gradient(180deg,#06192b 0%,#0b2a45 60%,#0a2a45 100%)}
.hero-title{position:absolute;left:145px;top:140px;font-family:"Cinzel",serif;font-weight:500;font-size:70px;line-height:78px;color:#fff}
.hero-dots{position:absolute;left:1118px;top:240px;display:flex;flex-direction:column;gap:10px}
.hero-dots span{width:9px;height:9px;border-radius:50%;background:#fff}
.hero-dots span.on{background:var(--blue-bright)}
.hero-curve{position:absolute;left:0;top:0}

.btn{position:absolute;height:62px;border-radius:31px;font-size:14.5px;font-weight:500;text-transform:uppercase;display:flex;align-items:center;justify-content:center}
.btn-apply{background:var(--blue-btn);color:#fff}
.btn-book-light{border:3px solid #fff;color:#fff}
.btn-book-blue{border:3px solid var(--blue-btn);color:var(--blue-btn)}

/* about */
.about-title{position:absolute;left:0;width:1200px;text-align:center;font-family:"Cinzel",serif;font-weight:400}
.about-title.main{top:762px;font-size:60px;color:#111}
.about-title.sub{top:830px;font-size:44px;color:var(--blue-btn)}
.about-copy{position:absolute;left:200px;top:918px;width:800px;text-align:center;font-size:12.5px;line-height:28px;color:var(--text)}

/* feature sections */
.photo{position:absolute;width:599px;height:506px}
.card{position:absolute;width:549px;height:391px;background:#fff;box-shadow:0 4px 24px rgba(0,0,0,.09);padding:33px 55px 0}
.card h2{font-weight:500;font-size:29px;line-height:40px;color:#111;width:400px}
.ticks{list-style:none;margin-top:24px}
.ticks li{position:relative;padding-left:31px;font-size:13.5px;line-height:27px;color:#333}
.ticks li::before{content:"";position:absolute;left:0;top:8px;width:11px;height:11px;border:1.6px solid var(--blue-btn);border-radius:50%}
.ticks li::after{content:"";position:absolute;left:4.3px;top:10.5px;width:3px;height:5px;border:solid var(--blue-btn);border-width:0 1.6px 1.6px 0;transform:rotate(45deg)}
.card .note{margin-top:18px;font-size:12.5px;line-height:24px;color:var(--text)}
.cols{display:flex}
.cols .ticks:first-child{width:160px}

/* footer */
.footer{position:absolute;left:0;top:2960px;width:1200px;height:461px;background:var(--footer);color:#fff}
.footer-edge{position:absolute;left:0;top:0}
.f-head{position:absolute;font-size:18px;font-weight:500;text-transform:uppercase;color:#fff}
.f-links{position:absolute;list-style:none;font-size:12.5px}
.f-links a{color:#fff}
.f-contact{position:absolute;left:145px;font-size:12.5px;line-height:22px;padding-left:24px}
.f-contact svg{position:absolute;left:0;top:3px}
.copyright{position:absolute;left:540px;width:513px;top:394px;text-align:right;font-size:12.5px}
.copyright a{color:#fff}
</style>
</head>
<body>

<header class="header">
  <div class="topline"></div>
  <a class="brand" href="#"><span class="brand-mark"></span><span class="brand-name">Corven Ridge Finance</span></a>
  <nav class="nav">
    <a class="home" href="#">Home</a>
    <a class="about" href="#">About Us</a>
    <a class="solutions" href="#">Financing Solutions</a>
    <a class="contact" href="#">Contact Us</a>
  </nav>
</header>

<section class="hero" role="img" aria-label="Dotted world map over a glowing financial candlestick chart on a dark blue background">
  <h1 class="hero-title">Corven Ridge<br>Finance</h1>
  <a class="btn btn-apply" href="#" style="left:146px;top:349px;width:212px">Apply Now</a>
  <a class="btn btn-book-light" href="#" style="left:369px;top:349px;width:243px">Book an Appointment</a>
  <div class="hero-dots"><span></span><span></span><span class="on"></span><span></span><span></span></div>
  <svg class="hero-curve" width="1200" height="645" viewBox="0 0 1200 645">
    <polygon points="0,645 0,642 906,542 1200,645" fill="#fff"/>
    <polygon points="0,639 906,532 1200,640 1200,646 906,546 0,644" fill="#1677c5"/>
  </svg>
</section>

<section class="about">
  <h2 class="about-title main">About</h2>
  <h3 class="about-title sub">Corven Ridge Finance</h3>
  <p class="about-copy">Corven Ridge Finance was created by its founder and CEO, Mirela Dovanic, for the purpose of meeting the continued growing requirements of businesses for working capital solutions in the frame of operational efficiency, business growth and credit risk mitigation needs. Corven Ridge Finance brings global, regional and local experience in trade finance, supply chain finance and commodity finance to the marketplace and will be best placed to structure, tailor and provide a financing solution for your business.</p>
  <a class="btn btn-apply" href="#" style="left:366px;top:1075px;width:213px">Apply Now</a>
  <a class="btn btn-book-blue" href="#" style="left:589px;top:1075px;width:244px">Book an Appointment</a>
</section>

<section class="feature">
  <div class="photo" role="img" aria-label="Digital globe with a rising line chart over a glowing blue data grid" style="left:0;top:1227px;background:linear-gradient(135deg,#0a3a8c 0%,#1868d0 45%,#29a8e8 75%,#0c3f9a 100%)"></div>
  <div class="card" style="left:506px;top:1285px">
    <h2>Financing solutions that will be provided by Corven Ridge Finance will include:</h2>
    <ul class="ticks">
      <li>Receivables Finance, which includes:</li>
      <li>Receivables Financing</li>
      <li>Factoring</li>
      <li>Invoice Financing</li>
    </ul>
    <p class="note">with structured optionsof; disclosed, confidential, single debtor, single invoice, multi debtor or total pool purchase financing available.</p>
  </div>
</section>

<section class="feature">
  <div class="photo" role="img" aria-label="Hand holding a glass globe surrounded by glowing currency symbols" style="left:601px;top:1809px;background:radial-gradient(circle at 300px 210px,#cfe8ff 0%,#3f8fd6 22%,#123f86 55%,#0a2258 100%)"></div>
  <div class="card" style="left:143px;top:1867px">
    <h2 style="width:450px">The financing solutions mentioned above will assist businesses to</h2>
    <ul class="ticks">
      <li>monetise its receivables to accelerate its cash cycle</li>
      <li>mitigate debtor credit risk</li>
      <li>minimise payment risks</li>
      <li>optimise credit limits so as to boost sales growth</li>
      <li>use its working capital to fund its business</li>
    </ul>
  </div>
</section>

<section class="feature">
  <div class="photo" role="img" aria-label="Silhouettes of business people among glowing digital data graphics" style="left:0;top:2389px;background:linear-gradient(135deg,#1a4fa8 0%,#3c8fd8 40%,#f0c8a8 55%,#2a5cb5 75%,#122c78 100%)"></div>
  <div class="card" style="left:506px;top:2446px">
    <h2>The industry sectors focussed on are, but not limited to</h2>
    <div class="cols">
      <ul class="ticks">
        <li>Infrastructure</li>
        <li>Resources</li>
        <li>FMCG</li>
        <li>Industrial</li>
        <li>Services</li>
      </ul>
      <ul class="ticks">
        <li>Information Technology</li>
        <li>Telecomm</li>
        <li>Consulting</li>
        <li>Construction</li>
      </ul>
    </div>
    <p class="note">We look forward to providing financing solutions that will answer your working capital needs.</p>
  </div>
</section>

<footer class="footer">
  <svg class="footer-edge" width="1200" height="120" viewBox="0 0 1200 120">
    <polygon points="0,0 1200,0 1200,3 295,113 0,8" fill="#fff"/>
    <polyline points="0,6 295,114 1200,2" fill="none" stroke="#1677c5" stroke-width="6"/>
  </svg>
  <a class="btn btn-apply" href="#" style="left:145px;top:183px;width:212px">Apply Now</a>
  <a class="btn btn-book-light" href="#" style="left:366px;top:181px;width:248px;height:66px;border-radius:33px">Book an Appointment</a>

  <h4 class="f-head" style="left:144px;top:283px">Contact Info</h4>
  <p class="f-contact" style="top:329px">
    <svg width="12" height="16" viewBox="0 0 12 16"><path d="M6 0C2.7 0 0 2.6 0 5.9 0 10.3 6 16 6 16s6-5.7 6-10.1C12 2.6 9.3 0 6 0zm0 8.2A2.3 2.3 0 1 1 6 3.6a2.3 2.3 0 0 1 0 4.6z" fill="#1a8ee0"/></svg>
    Office Level 4, 218 Harbourview Crescent,<br>NSW 2031, Australia
  </p>
  <p class="f-contact" style="top:392px">
    <svg width="14" height="14" viewBox="0 0 14 14"><path d="M3 0.5l2.2 3-1.3 1.6c.9 1.9 2.4 3.4 4.3 4.3l1.6-1.3 3 2.2-1.2 2.6C6.2 13 1 7.8.5 1.7z" fill="#1a8ee0"/></svg>
    info@corvenridgefinance.com
  </p>

  <h4 class="f-head" style="left:699px;top:178px">Quick Links</h4>
  <ul class="f-links" style="left:700px;top:224px;line-height:24px">
    <li><a href="#">Home</a></li>
    <li><a href="#">About Us</a></li>
    <li><a href="#">Financing Solutions</a></li>
    <li><a href="#">Contact Us</a></li>
  </ul>

  <h4 class="f-head" style="left:926px;top:178px">Social Media</h4>
  <ul class="f-links" style="left:927px;top:224px;line-height:31px">
    <li><a href="#">Peerlane</a></li>
    <li><a href="#">Circlehall</a></li>
    <li><a href="#">Shortwire</a></li>
  </ul>

  <p class="copyright">© 2021 Corven Ridge Finance. All rights reserved.<a href="#">Privacy Policy</a> &nbsp;|&nbsp; <a href="#">Terms and Conditions</a></p>
</footer>

</body>
</html>
```